Young Balance Support Network

We need a poster explaining that some children live with a disability called Vestibular Disorder. Feel free to ask question. We want you to respect our color code, same as our logo.

Here is our website : http://www.ybsnetwork.org/

We need to sensibilise people about this disability for children.

Industry/Entity Type

Charity

Font styles to use
Serif

Requirements
Must have
• 1. our logo (with all our details) + one of the photo of Marek
• 2. design showing a child with a dizziness for exemple
• 3. a title saying : Aidez-nous à changer la vie des enfants vivant avec un problème vestibulaire
• 4.include the text attached (information flyer YBSN)
• Poster size : 24"X 36"
Should not have
• wheel chair

```html
<!DOCTYPE html>
<html lang="fr">
<head>
<meta charset="utf-8">
<title>YBSN – Affiche vestibulaire</title>
<link href="https://fonts.googleapis.com/css2?family=Exo+2:wght@400;600;700&family=Lato:wght@400;700&family=Roboto+Condensed:wght@400;700&display=swap" rel="stylesheet">
<style>
  :root {
    --backdrop: #3b2c24;
    --poster-white: #ffffff;
    --photo-red: #c73a26;
    --photo-red-light: #e05a3f;
    --photo-skin: #f0b9a0;
    --photo-hair: #8a4a32;
    --cloud-orange: #f5a623;
    --title-orange: #f5a623;
    --title-blue: #29abe2;
    --pill-green: #a8c61a;
    --logo-green: #c5d92d;
    --body-text: #2a2a2a;
    --sky-blue: #bfe3f7;
    --box-navy: #1f4a7a;
    --box-yellow: #e8e03a;
    --grass-light: #9be04a;
    --grass-mid: #6cc22c;
    --grass-dark: #3c9a1c;
  }
  * { box-sizing: border-box; margin: 0; padding: 0; }
  html, body { width: 1200px; height: 1200px; overflow: hidden; background: var(--backdrop); }
  .poster {
    position: absolute; left: 220px; top: 30px; width: 760px; height: 1140px;
    background: linear-gradient(to bottom, var(--poster-white) 520px, var(--sky-blue) 1000px, var(--sky-blue));
    overflow: hidden; font-family: "Lato", sans-serif; color: var(--body-text);
    box-shadow: 0 6px 24px rgba(0,0,0,.5);
  }
  .hero {
    position: absolute; left: 0; top: 0; width: 760px; height: 480px;
    background: radial-gradient(ellipse at 70% 40%, var(--photo-red-light), var(--photo-red) 70%);
  }
  .hero-photo {
    position: absolute; left: 250px; top: 50px; width: 460px; height: 430px;
    border-radius: 48% 48% 0 0 / 40% 40% 0 0;
    background:
      radial-gradient(ellipse 34% 30% at 52% 48%, var(--photo-skin) 0%, rgba(240,185,160,.6) 55%, rgba(240,185,160,0) 100%),
      radial-gradient(ellipse 60% 55% at 50% 45%, var(--photo-hair) 0%, rgba(138,74,50,.5) 60%, rgba(138,74,50,0) 100%),
      linear-gradient(to bottom, rgba(199,58,38,0) 60%, rgba(170,40,30,.7) 100%);
  }
  .cloud-edge { position: absolute; left: 0; top: 440px; width: 760px; height: 60px; }
  .brand {
    position: absolute; left: 62px; top: 232px; display: flex; align-items: center; gap: 12px;
  }
  .brand-dot { width: 36px; height: 36px; border-radius: 50%; background: var(--logo-green); }
  .brand-name {
    font-family: "Exo 2", sans-serif; font-weight: 600; font-size: 44px;
    letter-spacing: 3px; color: var(--logo-green);
  }
  .headline {
    position: absolute; left: 0; top: 508px; width: 760px; text-align: center;
    font-family: "Exo 2", sans-serif; font-weight: 700; font-size: 30px; line-height: 36px;
  }
  .headline .line-orange { color: var(--title-orange); display: block; }
  .headline .line-blue { color: var(--title-blue); display: block; }
  .pill {
    position: absolute; display: inline-block; background: var(--pill-green); color: #fff;
    font-family: "Exo 2", sans-serif; font-size: 13.5px; padding: 3px 12px; border-radius: 0 12px 12px 0;
    white-space: nowrap;
  }
  .copy { position: absolute; font-size: 10.2px; line-height: 13.2px; text-align: justify; }
  .copy p + p { margin-top: 11px; }
  .col-left { left: 35px; width: 324px; }
  .col-right { left: 398px; width: 324px; }
  .name-box {
    position: absolute; left: 398px; top: 766px; width: 362px; height: 101px;
    background: var(--box-navy); padding: 12px 0 0 16px;
  }
  .name-box .line-top { font-family: "Exo 2", sans-serif; font-size: 29px; color: #fff; line-height: 38px; white-space: nowrap; }
  .name-box .line-bottom {
    font-family: "Roboto Condensed", sans-serif; font-weight: 700; font-size: 30px;
    color: var(--box-yellow); line-height: 40px; letter-spacing: .3px;
  }
  .contacts { position: absolute; left: 398px; top: 886px; font-size: 12.5px; }
  .contact-row { display: flex; align-items: center; gap: 10px; height: 26px; }
  .contact-row svg { width: 16px; height: 16px; }
  .ccp-label { font-family: "Roboto Condensed", sans-serif; font-weight: 700; font-size: 10px; width: 16px; }
  .social { position: absolute; top: 911px; display: flex; align-items: center; justify-content: center;
    width: 42px; height: 42px; background: var(--box-navy); color: #fff; font-size: 6.5px; font-weight: 700; }
  .social.friend { left: 619px; }
  .social.chirp { left: 678px; background: var(--title-blue); }
  .grass {
    position: absolute; left: 0; top: 975px; width: 760px; height: 165px;
    background:
      linear-gradient(to bottom, rgba(155,224,74,0) 0%, rgba(155,224,74,.75) 22%, var(--grass-light) 40%, var(--grass-mid) 70%, var(--grass-dark) 100%);
  }
</style>
</head>
<body>
<main class="poster">
  <div class="hero"></div>
  <div class="hero-photo" role="img" aria-label="Photo d'une petite fille aux yeux fermés, mains sur les tempes, portant un bandeau rouge à fleurs blanches, prise de vertige"></div>
  <svg class="cloud-edge" viewBox="0 0 760 60" preserveAspectRatio="none" aria-hidden="true">
    <path d="M0 60 L0 28 Q20 10 45 24 Q70 6 100 22 Q130 8 160 20 Q190 14 215 24 Q245 0 280 18 Q315 4 345 20 Q380 30 410 20 Q440 8 470 24 Q500 30 525 18 Q555 0 590 22 Q615 30 640 22 Q675 6 705 24 Q730 6 760 18 L760 60 Z" fill="#ffffff" stroke="var(--cloud-orange)" stroke-width="3"/>
  </svg>
  <div class="brand">
    <span class="brand-dot"></span>
    <span class="brand-name">YBSN</span>
  </div>

  <h1 class="headline">
    <span class="line-orange">Aidez-nous à changer la vie des enfants</span>
    <span class="line-blue">vivant avec un problème vestibulaire</span>
  </h1>

  <span class="pill" style="left:35px;top:616px">Qu'est-ce que le vestibule ?</span>
  <div class="copy col-left" style="top:653px">
    <p>C'est un organe sensoriel, pilier de votre équilibre, véritable 6ème sens situé dans l'oreille interne.</p>
  </div>

  <span class="pill" style="left:35px;top:690px">Qu'est ce qu'une aréflexie vestibulaire ?</span>
  <div class="copy col-left" style="top:728px">
    <p>C'est l'absence complète de toute information vestibulaire. L'enfant a ainsi l'impression que tout vacille autour de lui, jour et nuit.</p>
  </div>

  <span class="pill" style="left:35px;top:767px">Quelles en sont les conséquences pour l'enfant ?</span>
  <div class="copy col-left" style="top:804px">
    <p>Le développement moteur de l'enfant est retardé car il doit trouver des solutions afin de construire son équilibre, stabiliser son regard et son corps.</p>
    <p>Certains apprentissages sont de véritables obstacles pour l'enfant : se représenter son propre corps, se situer dans l'espace qui l'entoure, interagir avec les autres, communiquer, écrire, lire, manger, boire, marcher. Chacune de ces actions nécessitent des efforts considérables pour se concentrer quelques secondes ou minutes.</p>
    <p>Quand l'enfant réussit à effectuer l'une de ces actions, son comportement peut sembler déroutant et bien trop souvent mal interprété par le grand public.</p>
  </div>

  <span class="pill" style="left:398px;top:607px">Quel est le but de notre association ?</span>
  <div class="copy col-right" style="top:651px">
    <p>Notre association a pour but de promouvoir les troubles vestibulaires chez l'enfant, ses conséquences sur sa santé ainsi que celui de son entourage et de soutenir ces enfants et leurs parents en leur offrant un espace de parole et des solutions concrètes pour soulager leur quotidien. Notre association a également pour but de financer et promouvoir toute action de recherche scientifique visant à aider les enfants ayant un trouble vestibulaire.</p>
  </div>

  <div class="name-box">
    <div class="line-top">Young Balance Support</div>
    <div class="line-bottom">NETWORK</div>
  </div>

  <div class="contacts">
    <div class="contact-row">
      <svg viewBox="0 0 16 16" aria-hidden="true"><rect x="1" y="3" width="14" height="10" fill="none" stroke="#1f4a7a" stroke-width="1.6"/><path d="M1 3 L8 9 L15 3" fill="none" stroke="#1f4a7a" stroke-width="1.6"/></svg>
      <span>info@ybsnetwork.org</span>
    </div>
    <div class="contact-row">
      <svg viewBox="0 0 16 16" aria-hidden="true"><circle cx="8" cy="8" r="6.5" fill="none" stroke="#1f4a7a" stroke-width="1.4"/><ellipse cx="8" cy="8" rx="3" ry="6.5" fill="none" stroke="#1f4a7a" stroke-width="1.2"/><path d="M1.5 8 H14.5" stroke="#1f4a7a" stroke-width="1.2"/></svg>
      <span>www.ybsnetwork.org</span>
    </div>
    <div class="contact-row">
      <span class="ccp-label">CCP:</span>
      <span>12-345678-9</span>
    </div>
  </div>

  <span class="social friend">FriendPage</span>
  <span class="social chirp">ChirpLine</span>

  <div class="grass" role="img" aria-label="Illustration d'une bande d'herbe verte fraîche au bas de l'affiche"></div>
</main>
</body>
</html>
```